Multivitamin fruit drink in tetrapak

Label design for a 200 ml tetrapak which contains fruit juice with multivitamins in natural form . Product will be promoted to doctors and will follow a otx model. The target is children and women. Being a completely natural fortified multivitamin and mineral drink , the natural aspects to be highlighted. A white background is suggestive . Should not have more than 6 colors as this involves flexo printing.

Target Market(s)

Children and women through doctors recommendations

Industry/Entity Type

Pharmaceutical

Font styles to use
Serif
Sans Serif
Decorative

Requirements
Must have
• Pictures of fruit . Variant 1 is mango and variant 2 is orange. Brand name is Verosta. Can also suggest new names.
Nice to have
• The brand standing out, with white or softer color background
Should not have
• Should not have Dark background. Not funky or too colorful.

```html
<!DOCTYPE html>
<html lang="en">
<head>
<meta charset="UTF-8">
<title>Verosta Orange – 200 ml Pack Label</title>
<link rel="stylesheet" href="https://fonts.googleapis.com/css2?family=Asap:ital,wght@0,400;0,700;1,600&family=Montserrat:wght@700;800&display=swap">
<style>
  :root {
    --backdrop: #e9e9ea;
    --pack-white: #ffffff;
    --pack-orange: #eea51c;
    --pack-orange-deep: #e08d12;
    --citrus: #f39a2b;
    --citrus-light: #fbc062;
    --leaf-green: #3f8a2e;
    --label-green: #2f5a2a;
    --label-orange: #f2a01a;
  }
  * { box-sizing: border-box; margin: 0; padding: 0; }
  html, body {
    width: 848px;
    height: 1200px;
    overflow: hidden;
    background: var(--backdrop);
  }
  .canvas {
    position: relative;
    width: 848px;
    height: 1200px;
  }
  .pack-front {
    position: absolute;
    left: 184px;
    top: 70px;
    width: 480px;
    height: 1060px;
    background: var(--pack-white);
    overflow: hidden;
    box-shadow: 0 10px 30px rgba(0,0,0,0.12);
  }
  .band {
    position: absolute;
    left: 0;
    width: 480px;
  }
  .band--top { top: 0; height: 130px; }
  .band--bottom { top: 720px; height: 340px; }
  .brand-name {
    position: absolute;
    top: 150px;
    left: 0;
    width: 100%;
    text-align: center;
    font-family: "Asap", sans-serif;
    font-weight: 700;
    font-size: 54px;
    color: var(--leaf-green);
    letter-spacing: 0.5px;
  }
  .fruit-art {
    position: absolute;
    left: 70px;
    top: 262px;
    width: 340px;
    height: 440px;
    border-radius: 46% 46% 44% 44%;
    background:
      radial-gradient(circle at 30% 28%, var(--citrus-light) 0%, var(--citrus) 45%, transparent 70%),
      radial-gradient(circle at 72% 30%, var(--citrus-light) 0%, var(--citrus) 45%, transparent 70%),
      radial-gradient(circle at 50% 70%, var(--citrus-light) 0%, var(--citrus) 42%, transparent 68%),
      radial-gradient(ellipse at 50% 50%, rgba(93,160,60,0.55) 0%, transparent 70%);
  }
  .variant-label {
    position: absolute;
    left: 120px;
    top: 408px;
    width: 240px;
    height: 105px;
    left: 120px;
    width: 322px;
    left: 79px;
    background: var(--pack-white);
    border: 3px solid var(--pack-orange);
    text-align: center;
    padding-top: 8px;
  }
  .variant-label__fruit {
    font-family: "Montserrat", sans-serif;
    font-weight: 800;
    font-size: 52px;
    line-height: 1;
    color: var(--label-orange);
    letter-spacing: 1px;
  }
  .variant-label__type {
    font-family: "Montserrat", sans-serif;
    font-weight: 700;
    font-size: 24px;
    line-height: 1.3;
    color: var(--label-green);
    margin-top: 4px;
  }
  .claim {
    position: absolute;
    top: 790px;
    left: 0;
    width: 100%;
    text-align: center;
    font-family: "Asap", sans-serif;
    font-style: italic;
    font-weight: 600;
    font-size: 27px;
    line-height: 1.3;
    color: var(--pack-white);
  }
  .net-volume {
    position: absolute;
    top: 920px;
    left: 0;
    width: 100%;
    text-align: center;
    font-family: "Asap", sans-serif;
    font-weight: 400;
    font-size: 25px;
    color: var(--pack-white);
  }
</style>
</head>
<body>
<main class="canvas">
  <section class="pack-front">
    <svg class="band band--top" viewBox="0 0 480 130" aria-hidden="true">
      <path d="M0 0 H480 V112 Q240 40 0 112 Z" fill="var(--pack-orange)"/>
    </svg>

    <h1 class="brand-name">Verosta</h1>

    <div class="fruit-art" role="img" aria-label="Sliced orange halves framed by green leaves with a drop of juice falling below"></div>

    <div class="variant-label">
      <p class="variant-label__fruit">ORANGE</p>
      <p class="variant-label__type">100% FRUIT JUICE</p>
    </div>

    <svg class="band band--bottom" viewBox="0 0 480 340" aria-hidden="true">
      <path d="M0 8 Q240 40 480 8 V340 H0 Z" fill="var(--pack-orange)"/>
    </svg>

    <p class="claim">fortified with natural<br>vitamins and minerals</p>
    <p class="net-volume">Net wt:200ml</p>
  </section>
</main>
</body>
</html>
```